Snapframe Party Rentals New Business Card*

Need a business card designed for a Photo Booth Hire company.Must look very professional and colorful.A new creative logo would be a bonus. Our current logo is attached on here.

Contact Information for Business Card

Business Name: SNAPFRAME PARTY RENTALS
Contact Person: MARCUS OKAFOR
Mobile: 0491862035
Email: INFO@SNAPFRAMEPARTY.EXAMPLE
Website: WWW.SNAPFRAMEPARTY.EXAMPLE
Facebook: WWW.SOCIALNET.EXAMPLE/SNAPFRAME.PARTY.RENT

Font styles to use
Serif
Sans Serif
Script

Colors

Designer to choose colors to be used in the design.

Requirements
Must have
• Bonus if the colors match our website.

```html
<!DOCTYPE html>
<html lang="en">
<head>
<meta charset="utf-8">
<title>Snapframe Party Rentals – Business Card</title>
<link href="https://fonts.googleapis.com/css2?family=Roboto:wght@400;700&display=swap" rel="stylesheet">
<style>
  :root {
    --bg: #d9dadb;
    --card-white: #ffffff;
    --brand-blue: #1e9ac4;
    --brand-orange: #f0681e;
    --text-grey: #555b60;
    --rule-grey: #e1e3e5;
  }
  * { box-sizing: border-box; margin: 0; padding: 0; }
  html, body {
    width: 1200px; height: 1200px; overflow: hidden;
    background: var(--bg);
    font-family: "Roboto", Arial, sans-serif;
  }
  .stage {
    position: relative; width: 1200px; height: 1200px;
    display: flex; justify-content: center; align-items: center; gap: 80px;
  }
  .card {
    width: 400px; height: 655px; position: relative;
    box-shadow: 0 6px 18px rgba(0,0,0,0.12);
  }
  .card--front { background: var(--card-white); }
  .card--back { background: var(--brand-blue); color: #fff; }

  .contact { position: absolute; top: 56px; left: 56px; right: 40px; }
  .contact__name {
    color: var(--brand-orange); font-weight: 700; font-size: 22px; letter-spacing: 1px;
  }
  .contact__role { color: var(--text-grey); font-size: 20px; margin-top: 2px; }
  .contact__list { list-style: none; margin-top: 18px; }
  .contact__item {
    display: flex; align-items: center; gap: 10px;
    color: var(--text-grey); font-size: 14px; line-height: 26px;
  }
  .contact__item svg { width: 15px; height: 15px; flex: none; }
  .contact__rule {
    position: absolute; top: 262px; left: 40px; right: 40px;
    height: 1px; background: var(--rule-grey);
  }

  .wordmark {
    position: absolute; left: 0; right: 0; top: 330px;
    display: flex; flex-direction: column; align-items: center; gap: 22px;
  }
  .wordmark__dot {
    width: 110px; height: 110px; border-radius: 50%;
    border: 14px solid var(--brand-blue);
  }
  .wordmark__name {
    color: var(--brand-blue); font-weight: 700; font-size: 34px;
    line-height: 1.1; text-align: center; letter-spacing: 0.5px;
  }

  .back-mark {
    position: absolute; top: 120px; left: 40px; right: 40px;
    font-weight: 700; font-size: 50px; line-height: 1.05;
    letter-spacing: 2px; text-align: center;
  }
  .back-url {
    position: absolute; bottom: 110px; left: 0; right: 0;
    text-align: center; font-size: 17px;
  }
</style>
</head>
<body>
<main class="stage">
  <section class="card card--front" aria-label="Business card front">
    <div class="contact">
      <p class="contact__name">MARCUS OKAFOR</p>
      <p class="contact__role">Contact Person</p>
      <ul class="contact__list">
        <li class="contact__item">
          <svg viewBox="0 0 16 16" aria-hidden="true"><rect x="1" y="3" width="14" height="10" rx="1" fill="#1e9ac4"/><path d="M1.5 4 L8 9 L14.5 4" stroke="#fff" stroke-width="1.4" fill="none"/></svg>
          info@snapframeparty.example
        </li>
        <li class="contact__item">
          <svg viewBox="0 0 16 16" aria-hidden="true"><path d="M4 1.5 L6.5 4.5 L5 6.5 C6 8.5 7.5 10 9.5 11 L11.5 9.5 L14.5 12 L12.5 14.5 C7 14 2 9 1.5 3.5 Z" fill="#1e9ac4"/></svg>
          0491862035
        </li>
        <li class="contact__item">
          <svg viewBox="0 0 16 16" aria-hidden="true"><rect x="1.5" y="1.5" width="13" height="13" rx="2" fill="#1e9ac4"/></svg>
          socialnet.example/snapframe.party.rent
        </li>
      </ul>
    </div>
    <div class="contact__rule"></div>
    <div class="wordmark">
      <div class="wordmark__dot"></div>
      <p class="wordmark__name">Snapframe<br>Party Rentals</p>
    </div>
  </section>

  <section class="card card--back" aria-label="Business card back">
    <p class="back-mark">SNAPFRAME<br>PARTY<br>RENTALS</p>
    <p class="back-url">www.snapframeparty.example</p>
  </section>
</main>
</body>
</html>
```